" Trabalhamos com call center e e-commerce. Diferente de demais empresas de produtos naturais, perguntamos qual o problema e entregamos uma solução pronta. Fazemos propagandas diversas e atendemos via 0800. Estamos reformulando a empresa e toda nossa linha de produtos em termos de linguagem visual. "

```html
<!DOCTYPE html>
<html lang="pt-BR">
<head>
<meta charset="utf-8">
<title>VitaGoji Green – rótulo</title>
<link rel="stylesheet" href="https://fonts.googleapis.com/css2?family=Roboto:wght@300;400;700;900&family=Roboto+Condensed:wght@400;700&display=swap">
<style>
  :root {
    --page-bg: #e6e7e9;
    --label-white: #f7f8f9;
    --silver-light: #eef0f2;
    --silver-mid: #c7ccd2;
    --silver-dark: #9aa2ab;
    --brand-blue: #1f4b8e;
    --deep-blue: #17336b;
    --navy: #0f234d;
    --ink: #1a2a4a;
    --grey-text: #7e8791;
    --white: #ffffff;
  }
  * { margin: 0; padding: 0; box-sizing: border-box; }
  html, body { width: 1200px; height: 1200px; overflow: hidden; }
  body {
    background: radial-gradient(circle at 50% 45%, #f4f5f6 0%, var(--page-bg) 70%);
    font-family: "Roboto", Arial, sans-serif;
    position: relative;
  }
  .label {
    position: absolute;
    left: 100px; top: 230px;
    width: 1000px; height: 740px;
    background: linear-gradient(180deg, var(--label-white) 0%, var(--silver-light) 100%);
    box-shadow: 0 18px 40px rgba(30, 40, 60, 0.18);
    overflow: hidden;
  }
  .label-bands { position: absolute; inset: 0; }

  .warning-panel {
    position: absolute;
    left: 34px; top: 60px;
    width: 180px;
    font-family: "Roboto Condensed", Arial, sans-serif;
    font-size: 15px;
    line-height: 1.55;
    color: var(--grey-text);
    text-align: right;
    text-transform: uppercase;
    letter-spacing: 0.3px;
  }

  .brand {
    position: absolute;
    left: 262px; top: 48px;
    display: flex; align-items: center; gap: 10px;
  }
  .brand-dot {
    width: 26px; height: 26px; border-radius: 50%;
    background: var(--brand-blue);
  }
  .brand-name {
    font-size: 34px; font-weight: 400; color: var(--brand-blue);
    letter-spacing: 0.5px;
  }

  .product-name {
    position: absolute;
    left: 300px; top: 172px;
    font-size: 58px; font-weight: 900;
    letter-spacing: -0.5px;
    color: var(--deep-blue);
    line-height: 1;
  }
  .product-name .variant { color: var(--silver-dark); }
  .product-tagline {
    position: absolute;
    left: 480px; top: 234px;
    font-size: 24px; font-weight: 700; font-style: italic;
    color: var(--brand-blue);
  }

  .flask-art {
    position: absolute;
    left: 600px; top: 290px;
    width: 300px; height: 170px;
    border-radius: 50%;
    background: radial-gradient(ellipse at center, rgba(120, 160, 220, 0.35) 0%, rgba(31, 75, 142, 0) 70%);
  }

  .category {
    position: absolute;
    left: 300px; top: 380px;
    font-size: 24px; font-weight: 400; color: var(--white);
  }
  .ingredients {
    position: absolute;
    left: 300px; top: 412px;
    font-size: 23px; font-weight: 700; color: var(--white);
    letter-spacing: 0.3px;
  }

  .feature-row {
    position: absolute;
    left: 300px; top: 492px;
    width: 660px; height: 96px;
    display: flex; align-items: center;
    color: var(--white);
  }
  .feature {
    font-size: 20px; font-weight: 700; line-height: 1.2;
    text-transform: uppercase;
  }
  .feature-tech { width: 270px; }
  .feature-daily { width: 200px; padding-left: 26px; border-left: 2px solid var(--silver-mid); }
  .feature-count {
    padding-left: 26px; border-left: 2px solid var(--silver-mid);
    font-size: 56px; font-weight: 900;
  }

  .contact {
    position: absolute;
    left: 560px; top: 632px;
    text-align: center;
    color: var(--ink);
    font-weight: 700;
  }
  .contact-phone { font-size: 30px; letter-spacing: 1px; }
  .contact-web { font-size: 26px; }
</style>
</head>
<body>
  <div class="label">
    <svg class="label-bands" width="1000" height="740" viewBox="0 0 1000 740" aria-hidden="true">
      <defs>
        <linearGradient id="blueBand" x1="0" y1="0" x2="0" y2="1">
          <stop offset="0" stop-color="#2a5aa6"/>
          <stop offset="1" stop-color="#163466"/>
        </linearGradient>
        <linearGradient id="silverStrip" x1="0" y1="0" x2="0" y2="1">
          <stop offset="0" stop-color="#ffffff"/>
          <stop offset="0.5" stop-color="#dfe3e7"/>
          <stop offset="1" stop-color="#b9c0c8"/>
        </linearGradient>
        <linearGradient id="navyBand" x1="0" y1="0" x2="0" y2="1">
          <stop offset="0" stop-color="#15305f"/>
          <stop offset="1" stop-color="#0c1d40"/>
        </linearGradient>
      </defs>
      <!-- main blue field -->
      <path d="M250 140 H1000 V610 H250 Q236 375 250 140 Z" fill="url(#blueBand)"/>
      <!-- silver title strip -->
      <path d="M270 158 H1000 V272 H290 Q270 272 270 215 Z" fill="url(#silverStrip)"/>
      <!-- curved swoosh under title -->
      <path d="M250 300 Q560 262 1000 300 V316 Q560 280 250 318 Z" fill="#8fb0e0" opacity="0.35"/>
      <!-- navy feature band -->
      <rect x="250" y="478" width="750" height="124" fill="url(#navyBand)"/>
      <line x1="250" y1="478" x2="1000" y2="478" stroke="#c7ccd2" stroke-width="3"/>
      <line x1="250" y1="602" x2="1000" y2="602" stroke="#c7ccd2" stroke-width="3"/>
    </svg>

    <p class="warning-panel">Não contém glúten. Este produto não é um medicamento. Conservar em local seco e fresco. Gestantes, nutrizes e crianças: consumir somente sob orientação do nutricionista ou médico. Manter fora do alcance de crianças.</p>

    <div class="brand">
      <span class="brand-dot"></span>
      <span class="brand-name">remedia</span>
    </div>

    <h1 class="product-name">VITAGOJI <span class="variant">GREEN</span></h1>
    <p class="product-tagline">Goji Berry com Café Verde</p>

    <div class="flask-art" role="img" aria-label="Ilustração suave de um frasco de laboratório com bolhas"></div>

    <p class="category">Suplemento</p>
    <p class="ingredients">ACEROLA • CAFÉ VERDE • GOJI BERRY • VITAMINA C</p>

    <div class="feature-row">
      <div class="feature feature-tech">Gel Caps<br>Advanced<br>Technology</div>
      <div class="feature feature-daily">Fórmula<br>Diária</div>
      <div class="feature-count">60</div>
    </div>

    <div class="contact">
      <p class="contact-phone">0800 555 0199</p>
      <p class="contact-web">www.remedia.com</p>
    </div>
  </div>
</body>
</html>
```